Organic Vegan Crispread - 100% Free of Soja

We are looking to update our labels for our current range of Crispbreads. They are all produced in Denmark, they are organic, vegan og we do not use any soy at all.

The crisp breads are high products and aimed for the gourmet market retail.

The range contains 6 different at the moment and will have 4 new types coming soon. The current six products are following:
Organic Crispbread Salt
Organic Crispbread Herbs
Organic Crispbread spices
Organic Crispbread Seaweed
Organic Crispbread Glutenfree
Organic Cripsbread Protein (Green Proteins)

The range will have to contain our logo and our name.

Measurements of Labels:
60mm wide
50mm High

Only front label design.

Target Market(s)

High End Consumers

Requirements
Must have
• Company Logo
Organic logo red (under this we need to write "QX-VAL-738")
Organic logo Green (under this we need to write "EU / ikke EU-jordbrug")
Name
Visuel identity per type
Nice to have
• Red line throughout the range
Should not have
• No Bling Bling

```html
<!DOCTYPE html>
<html lang="en">
<head>
<meta charset="utf-8">
<title>Organic Crispbread – Label Range</title>
<link rel="stylesheet" href="https://fonts.googleapis.com/css2?family=Montserrat:wght@500;600;700&family=Oswald:wght@500&family=Playfair+Display:ital,wght@1,700;1,800&family=Source+Serif+4:wght@300&display=swap">
<style>
  :root {
    --backdrop: #a67c52;
    --paper: #ffffff;
    --ink: #1d1d1b;
    --brand-red: #e3232f;
    --seal-gold: #c2a27c;
    --eu-green: #9ccf3c;
    --sticker-green: #3fb54a;
  }
  * { box-sizing: border-box; margin: 0; padding: 0; }
  html, body { width: 1200px; height: 1200px; overflow: hidden; }
  body { background: var(--backdrop); position: relative; font-family: "Montserrat", sans-serif; }

  .label {
    position: absolute;
    width: 384px; height: 319px;
    background: var(--paper);
    box-shadow: 6px 8px 10px rgba(60, 35, 15, 0.35);
    overflow: hidden;
  }
  .label--salt      { left: 176px; top: 80px;  --accent: #223f8f; --strip-a: #5b8fd6; --strip-b: #4573c2; }
  .label--seaweed   { left: 640px; top: 80px;  --accent: #12877f; --strip-a: #7dd0c4; --strip-b: #5fbfb2; }
  .label--herbs     { left: 176px; top: 440px; --accent: #16884a; --strip-a: #7ec78f; --strip-b: #5cb074; }
  .label--glutenfree{ left: 640px; top: 440px; --accent: #55409a; --strip-a: #a197cc; --strip-b: #8c80bf; }
  .label--spices    { left: 176px; top: 800px; --accent: #84401e; --strip-a: #d8ad5f; --strip-b: #c99545; }
  .label--protein   { left: 640px; top: 800px; --accent: #ef5a29; --strip-a: #f3cc9c; --strip-b: #eeb983; }

  .flavour-strip {
    position: absolute; left: 289px; top: 0;
    width: 95px; height: 100%;
    background: linear-gradient(180deg, var(--strip-a), var(--strip-b));
  }

  .claims { position: absolute; left: 13px; top: 18px; list-style: none; }
  .claims li {
    display: flex; align-items: center; gap: 6px;
    font-size: 20px; font-weight: 500; color: var(--ink);
    line-height: 25px;
  }
  .claims svg { width: 20px; height: 20px; flex: none; }

  .brand-seal {
    position: absolute; left: 183px; top: 14px;
    width: 114px; height: 114px;
    border-radius: 50%;
    border: 3px solid var(--seal-gold);
    background: var(--paper);
    display: flex; align-items: center; justify-content: center;
    text-align: center;
  }
  .brand-seal__name {
    font-family: "Montserrat", sans-serif;
    font-weight: 600; font-size: 11px; letter-spacing: 1.5px;
    line-height: 15px; color: var(--seal-gold);
    text-transform: uppercase;
  }

  .product-organic {
    position: absolute; left: 13px; top: 88px;
    font-size: 29px; font-weight: 600; letter-spacing: 2.5px;
    color: var(--brand-red);
  }
  .product-name {
    position: absolute; left: 12px; top: 126px;
    font-family: "Oswald", sans-serif; font-weight: 500;
    font-size: 62px; line-height: 62px; letter-spacing: -1px;
    color: var(--ink);
  }
  .product-flavour {
    position: absolute; left: 13px; top: 174px;
    font-family: "Playfair Display", serif; font-style: italic; font-weight: 800;
    font-size: 42px; line-height: 46px; letter-spacing: 1px;
    color: var(--accent);
  }

  .soya-band {
    position: absolute; left: 0; top: 223px;
    width: 275px; height: 30px;
    background: var(--accent);
    color: #fff;
    font-family: "Source Serif 4", serif; font-weight: 300;
    font-size: 23px; line-height: 30px;
    padding-left: 13px;
  }

  .green-sticker {
    position: absolute; left: 200px; top: 183px;
    padding: 3px 8px;
    background: var(--sticker-green);
    border-radius: 6px;
    transform: rotate(-9deg);
    color: #fff; font-weight: 600; font-size: 13px; line-height: 13px;
    text-align: center;
  }

  .certifications { position: absolute; left: 13px; top: 265px; width: 262px; height: 41px; }
  .cert-eu { position: absolute; left: 0; top: 0; width: 69px; height: 41px; background: var(--eu-green); }
  .cert-national {
    position: absolute; left: 80px; top: 0;
    width: 42px; height: 41px; border-radius: 50%;
    background: var(--brand-red);
  }
  .origin {
    position: absolute; right: 0; top: 8px; text-align: left;
  }
  .origin__small { font-size: 8px; font-weight: 700; letter-spacing: 0.3px; color: var(--ink); line-height: 9px; }
  .origin__country { font-family: "Oswald", sans-serif; font-weight: 500; font-size: 17px; line-height: 19px; color: var(--ink); }
</style>
</head>
<body>

<!-- Reusable pieces are repeated per label -->

<section class="label label--salt">
  <div class="flavour-strip" role="img" aria-label="Blue wavy line pattern for the salt variety"></div>
  <ul class="claims">
    <li><svg viewBox="0 0 20 20"><path d="M2 5 L9 18 L18 2" fill="none" stroke="#e3232f" stroke-width="3.2" stroke-linejoin="round"/></svg>natural</li>
    <li><svg viewBox="0 0 20 20"><path d="M2 5 L9 18 L18 2" fill="none" stroke="#e3232f" stroke-width="3.2" stroke-linejoin="round"/></svg>vegan</li>
  </ul>
  <div class="brand-seal"><span class="brand-seal__name">Havlund<br>Organic<br>Goods</span></div>
  <p class="product-organic">organic</p>
  <h2 class="product-name">CRISPBREAD</h2>
  <p class="product-flavour">salt</p>
  <p class="soya-band">100% Free of Soya</p>
  <div class="certifications">
    <div class="cert-eu"></div>
    <div class="cert-national"></div>
    <div class="origin"><p class="origin__small">PRODUCED IN</p><p class="origin__country">DENMARK</p></div>
  </div>
</section>

<section class="label label--seaweed">
  <div class="flavour-strip" role="img" aria-label="Teal seaweed illustration for the seaweed variety"></div>
  <ul class="claims">
    <li><svg viewBox="0 0 20 20"><path d="M2 5 L9 18 L18 2" fill="none" stroke="#e3232f" stroke-width="3.2" stroke-linejoin="round"/></svg>natural</li>
    <li><svg viewBox="0 0 20 20"><path d="M2 5 L9 18 L18 2" fill="none" stroke="#e3232f" stroke-width="3.2" stroke-linejoin="round"/></svg>vegan</li>
  </ul>
  <div class="brand-seal"><span class="brand-seal__name">Havlund<br>Organic<br>Goods</span></div>
  <p class="product-organic">organic</p>
  <h2 class="product-name">CRISPBREAD</h2>
  <p class="product-flavour">seaweed</p>
  <p class="soya-band">100% Free of Soya</p>
  <div class="certifications">
    <div class="cert-eu"></div>
    <div class="cert-national"></div>
    <div class="origin"><p class="origin__small">PRODUCED IN</p><p class="origin__country">DENMARK</p></div>
  </div>
</section>

<section class="label label--herbs">
  <div class="flavour-strip" role="img" aria-label="Green leaf pattern for the herbs variety"></div>
  <ul class="claims">
    <li><svg viewBox="0 0 20 20"><path d="M2 5 L9 18 L18 2" fill="none" stroke="#e3232f" stroke-width="3.2" stroke-linejoin="round"/></svg>natural</li>
    <li><svg viewBox="0 0 20 20"><path d="M2 5 L9 18 L18 2" fill="none" stroke="#e3232f" stroke-width="3.2" stroke-linejoin="round"/></svg>vegan</li>
  </ul>
  <div class="brand-seal"><span class="brand-seal__name">Havlund<br>Organic<br>Goods</span></div>
  <p class="product-organic">organic</p>
  <h2 class="product-name">CRISPBREAD</h2>
  <p class="product-flavour">herbs</p>
  <p class="soya-band">100% Free of Soya</p>
  <div class="certifications">
    <div class="cert-eu"></div>
    <div class="cert-national"></div>
    <div class="origin"><p class="origin__small">PRODUCED IN</p><p class="origin__country">DENMARK</p></div>
  </div>
</section>

<section class="label label--glutenfree">
  <div class="flavour-strip" role="img" aria-label="Purple diagonal grain pattern for the gluten-free variety"></div>
  <ul class="claims">
    <li><svg viewBox="0 0 20 20"><path d="M2 5 L9 18 L18 2" fill="none" stroke="#e3232f" stroke-width="3.2" stroke-linejoin="round"/></svg>natural</li>
    <li><svg viewBox="0 0 20 20"><path d="M2 5 L9 18 L18 2" fill="none" stroke="#e3232f" stroke-width="3.2" stroke-linejoin="round"/></svg>vegan</li>
  </ul>
  <div class="brand-seal"><span class="brand-seal__name">Havlund<br>Organic<br>Goods</span></div>
  <p class="product-organic">organic</p>
  <h2 class="product-name">CRISPBREAD</h2>
  <p class="product-flavour">glutenfree</p>
  <p class="soya-band">100% Free of Soya</p>
  <div class="certifications">
    <div class="cert-eu"></div>
    <div class="cert-national"></div>
    <div class="origin"><p class="origin__small">PRODUCED IN</p><p class="origin__country">DENMARK</p></div>
  </div>
</section>

<section class="label label--spices">
  <div class="flavour-strip" role="img" aria-label="Ochre spice pattern with cinnamon sticks and star anise for the spices variety"></div>
  <ul class="claims">
    <li><svg viewBox="0 0 20 20"><path d="M2 5 L9 18 L18 2" fill="none" stroke="#e3232f" stroke-width="3.2" stroke-linejoin="round"/></svg>natural</li>
    <li><svg viewBox="0 0 20 20"><path d="M2 5 L9 18 L18 2" fill="none" stroke="#e3232f" stroke-width="3.2" stroke-linejoin="round"/></svg>vegan</li>
  </ul>
  <div class="brand-seal"><span class="brand-seal__name">Havlund<br>Organic<br>Goods</span></div>
  <p class="product-organic">organic</p>
  <h2 class="product-name">CRISPBREAD</h2>
  <p class="product-flavour">spices</p>
  <p class="soya-band">100% Free of Soya</p>
  <div class="certifications">
    <div class="cert-eu"></div>
    <div class="cert-national"></div>
    <div class="origin"><p class="origin__small">PRODUCED IN</p><p class="origin__country">DENMARK</p></div>
  </div>
</section>

<section class="label label--protein">
  <div class="flavour-strip" role="img" aria-label="Orange line-drawn leaf pattern for the protein variety"></div>
  <ul class="claims">
    <li><svg viewBox="0 0 20 20"><path d="M2 5 L9 18 L18 2" fill="none" stroke="#e3232f" stroke-width="3.2" stroke-linejoin="round"/></svg>natural</li>
    <li><svg viewBox="0 0 20 20"><path d="M2 5 L9 18 L18 2" fill="none" stroke="#e3232f" stroke-width="3.2" stroke-linejoin="round"/></svg>vegan</li>
  </ul>
  <div class="brand-seal"><span class="brand-seal__name">Havlund<br>Organic<br>Goods</span></div>
  <p class="product-organic">organic</p>
  <h2 class="product-name">CRISPBREAD</h2>
  <p class="product-flavour">protein</p>
  <p class="green-sticker">green<br>proteins</p>
  <p class="soya-band">100% Free of Soya</p>
  <div class="certifications">
    <div class="cert-eu"></div>
    <div class="cert-national"></div>
    <div class="origin"><p class="origin__small">PRODUCED IN</p><p class="origin__country">DENMARK</p></div>
  </div>
</section>

</body>
</html>
```